Logo Design - Wine Range

Hello Designers,
We need a graphic design for a new logo for a wine range that we are releasing in coming months and are wanting to design a logo that reflects the name in a unique and creative way.
The Name is HERON GLEN.
We are really wanting the Logo/label to have a visual element which in a quick glance it is visually symbolic and one to remember.
Brief
A )Label with be 10 cm length and 9cm width, wanting picture to be about 5cm in Length. Information on the front label needs to be Name - Heron Glen
B) Looking for BRIGHT AND BOLD colours that attract and relate to Australian Nature. Can also include Falcon Bird but not necessary.
The designer who is selected as winner will need to create a label in order to complete the project. Goodluck :)
Thank you for your interest, looking forward to reviewing designs soon.
Updates
Label with be 10 cm length and 9cm width, wanting picture to be about 5cm in Length. Information on the front label needs to be Name - Heron Glen
have attached a colour palette of Australian Nature for an idea of colour.
Target Market(s)
Age group 18+
Industry/Entity Type
Graphic Design
Requirements
Must have
- Must include a graphic design not just words
Nice to have
- Unique and modern touch, If using Falcon would like the bird to be whole, Australian Nature. Rocks, waterfalls... the sky is the limit really , goodluck

```html
<!DOCTYPE html>
<html lang="en">
<head>
<meta charset="utf-8">
<title>Heron Glen – Wine Label</title>
<link rel="stylesheet" href="https://fonts.googleapis.com/css2?family=Montserrat:wght@500&family=Poiret+One&display=swap">
<style>
  :root {
    --canvas-bg: #e9e9e9;
    --band-black: #1c1c1d;
    --band-inner: #232324;
    --rule-grey: #8a8a8c;
    --gold: #c9962e;
    --white: #f5f5f5;
    --pat-red: #e8384f;
    --pat-orange: #f47a20;
    --pat-yellow: #f6d64a;
    --pat-green: #7cc36b;
    --pat-teal: #2aa7a3;
    --pat-blue: #3d8fd6;
    --pat-pink: #e75a9b;
    --pat-purple: #8b5bb5;
  }
  * { box-sizing: border-box; margin: 0; padding: 0; }
  html, body {
    width: 750px;
    height: 1200px;
    overflow: hidden;
    background: var(--canvas-bg);
  }
  .canvas {
    position: relative;
    width: 750px;
    height: 1200px;
  }
  .label {
    position: absolute;
    left: 75px;
    top: 250px;
    width: 600px;
    height: 700px;
    display: flex;
    flex-direction: column;
    box-shadow: 0 6px 24px rgba(0,0,0,0.18);
  }
  .pattern { width: 100%; }
  .pattern--top {
    height: 80px;
    background: linear-gradient(90deg,
      var(--pat-teal) 0%, var(--pat-red) 18%, var(--pat-orange) 34%,
      var(--pat-yellow) 50%, var(--pat-pink) 68%, var(--pat-purple) 84%, var(--pat-blue) 100%);
  }
  .pattern--bottom {
    flex: 1;
    background:
      linear-gradient(180deg, rgba(255,255,255,0.08), rgba(0,0,0,0.08)),
      linear-gradient(90deg,
        var(--pat-blue) 0%, var(--pat-green) 16%, var(--pat-orange) 34%,
        var(--pat-yellow) 52%, var(--pat-pink) 70%, var(--pat-purple) 84%, var(--pat-blue) 100%);
  }
  .name-band {
    position: relative;
    height: 320px;
    background: var(--band-black);
  }
  .name-band__rule {
    position: absolute;
    left: 0;
    right: 0;
    height: 3px;
    background: var(--rule-grey);
  }
  .name-band__rule--top { top: 16px; }
  .name-band__rule--bottom { bottom: 16px; }
  .name-band__inner {
    position: absolute;
    left: 0;
    right: 0;
    top: 34px;
    bottom: 34px;
    background: var(--band-inner);
  }
  .brand-lockup {
    position: absolute;
    left: 36px;
    right: 36px;
    top: 34px;
    bottom: 34px;
    display: flex;
    align-items: center;
    justify-content: space-between;
    gap: 22px;
  }
  .brand-mark {
    flex: none;
    width: 76px;
    height: 76px;
    border-radius: 50%;
    background: var(--white);
  }
  .wordmark {
    text-align: right;
    white-space: nowrap;
  }
  .wordmark__tagline {
    font-family: "Montserrat", sans-serif;
    font-weight: 500;
    font-size: 17px;
    letter-spacing: 5px;
    color: var(--gold);
    margin-bottom: 10px;
  }
  .wordmark__name {
    font-family: "Poiret One", sans-serif;
    font-weight: 400;
    font-size: 72px;
    line-height: 1;
    letter-spacing: 2px;
    color: var(--white);
  }
</style>
</head>
<body>
  <main class="canvas">
    <section class="label">
      <div class="pattern pattern--top" role="img" aria-label="Bright geometric triangle pattern in Australian nature colours"></div>
      <div class="name-band">
        <div class="name-band__rule name-band__rule--top"></div>
        <div class="name-band__inner"></div>
        <div class="name-band__rule name-band__rule--bottom"></div>
        <div class="brand-lockup">
          <span class="brand-mark" aria-hidden="true"></span>
          <div class="wordmark">
            <p class="wordmark__tagline">PREMIUM WINE</p>
            <h1 class="wordmark__name">HERON GLEN</h1>
          </div>
        </div>
      </div>
      <div class="pattern pattern--bottom" role="img" aria-label="Bright geometric triangle pattern in Australian nature colours"></div>
    </section>
  </main>
</body>
</html>
```